Brannock Bay Ferry and Haulage

Need to redesign our business cards to relay that we do freight logistics and water taxi service. We also work with gov. agencies doing environmental clean up, oil spill response, remote site construction and work with many of the air taxi and helicopter services on Kodiak Island. Out website is www.brannockbayferry.com to get a better idea of what we do.

Contact Information for Business Card

I have a previous business card but it just has the logo on the front, and a sunset picture on the back with the contact info. It does not relay what we do and what we can help with. I like a simple straight forward design over a busy one.

Colors
3176b5
0455a3
cfdfed

Requirements
Must have
• logo, email, website, phone number

```html
<!DOCTYPE html>
<html lang="en">
<head>
<meta charset="utf-8">
<title>Brannock Bay Ferry and Haulage – Business Card</title>
<link rel="stylesheet" href="https://fonts.googleapis.com/css2?family=Open+Sans:wght@400;600;700&display=swap">
<style>
  :root {
    --navy: #0455a3;
    --deep: #123f8a;
    --sky: #3176b5;
    --mist: #cfdfed;
    --sun: #f0a024;
    --ink: #1c1c1c;
    --paper: #ffffff;
    --stage: #e4e7ec;
  }
  * { margin: 0; padding: 0; box-sizing: border-box; }
  html, body { width: 1200px; height: 900px; overflow: hidden; }
  body {
    background: var(--stage);
    font-family: "Open Sans", Arial, sans-serif;
    position: relative;
  }
  .card {
    position: absolute;
    left: 250px;
    width: 700px;
    height: 400px;
    overflow: hidden;
    box-shadow: 0 6px 18px rgba(0,0,0,.18);
  }
  .card--front { top: 35px; background: var(--paper); }
  .card--back {
    top: 465px;
    background: linear-gradient(160deg, var(--navy), var(--deep));
    display: flex; align-items: center; justify-content: center; gap: 18px;
  }
  .card__wave { position: absolute; inset: 0; }
  .brand {
    position: absolute; left: 48px; top: 44px;
    display: flex; align-items: center; gap: 12px;
  }
  .brand__dot { width: 26px; height: 26px; border-radius: 50%; background: var(--sun); }
  .brand__name {
    color: var(--navy); font-weight: 700; font-size: 24px; line-height: 1.15;
    width: 260px;
  }
  .divider {
    position: absolute; left: 40px; top: 150px; width: 560px; height: 1.5px;
    background: var(--sky);
  }
  .contacts {
    position: absolute; left: 40px; top: 170px; list-style: none;
    font-size: 15px; color: var(--ink); line-height: 26px;
  }
  .contacts li { display: flex; align-items: center; gap: 10px; }
  .contacts svg { width: 13px; height: 13px; fill: none; stroke: var(--navy); stroke-width: 1.8; }
  .person { position: absolute; right: 100px; top: 92px; text-align: right; }
  .person__name {
    color: var(--navy); font-weight: 600; font-size: 26px; letter-spacing: 1.5px;
    text-transform: uppercase;
  }
  .person__role { font-size: 17px; color: var(--ink); }
  .address {
    position: absolute; right: 100px; top: 162px; text-align: right;
    font-size: 15px; color: var(--ink); line-height: 22px;
  }
  .back__dot { width: 40px; height: 40px; border-radius: 50%; background: var(--sun); }
  .back__name { color: var(--paper); font-weight: 700; font-size: 38px; line-height: 1.15; width: 380px; }
</style>
</head>
<body>
  <section class="card card--front" aria-label="Business card front">
    <svg class="card__wave" viewBox="0 0 700 400" aria-hidden="true">
      <path d="M0,262 C160,330 370,300 470,340 C525,362 548,388 556,400 L0,400 Z" fill="var(--sun)"/>
      <path d="M0,272 C160,340 370,312 465,350 C515,370 536,390 542,400 L0,400 Z" fill="var(--navy)"/>
    </svg>

    <div class="brand">
      <span class="brand__dot"></span>
      <span class="brand__name">Brannock Bay Ferry and Haulage</span>
    </div>

    <div class="divider"></div>

    <ul class="contacts">
      <li><svg viewBox="0 0 14 14"><path d="M3 1.5l2 2.5-1.2 1.5c.8 1.8 2 3 3.7 3.7L9 8l2.5 2-1 2.5C6 12.5 1.5 8 1.5 3.5z"/></svg>907-555-0148</li>
      <li><svg viewBox="0 0 14 14"><rect x="1.5" y="3" width="11" height="8"/><path d="M1.5 3l5.5 4.5L12.5 3"/></svg>hello@brannockbayferry.com</li>
      <li><svg viewBox="0 0 14 14"><circle cx="7" cy="7" r="5.5"/><path d="M1.5 7h11M7 1.5c-3 3-3 8 0 11M7 1.5c3 3 3 8 0 11"/></svg>www.brannockbayferry.com</li>
    </ul>

    <div class="person">
      <p class="person__name">Dorian Vance</p>
      <p class="person__role">Director</p>
    </div>

    <address class="address">
      418 Harbor Crest Road<br>
      Tidewater, AK 99615
    </address>
  </section>

  <section class="card card--back" aria-label="Business card back">
    <span class="back__dot"></span>
    <span class="back__name">Brannock Bay Ferry and Haulage</span>
  </section>
</body>
</html>
```